galactic arcade 80s vibes - jewelry company

I am looking for someone to build me a website for my jewelry company - I am going for an 80s retro GALACTIC arcade vibe. I want it to feel old school, be brightly colored (purples, greens, etc) encompass planets, stars, or milky way type vibes. My company is called LunoVix - it is zodiac signs & angel number jewelry. I want the website to open up as galaxy and my logo/name to pop up in the center of the screen and then go to the main page.

Industry/Entity Type

jewelry

Coding

Coded - Design and coding required

Number of Pages Required

1 page

Font styles to use
Other font styles liked:
• retro

Colors
0094D4
00A9DD
6FCCEA
C7EBF8
E9F6FB
00AB8E
00BBA5
67D7C9
C6EFE9
E9F9F6
59FF00
82FF00
B8FF75
E3FFCB
F4FFEA
FFF300
FFF600
FEFA6F
FFFEC7
FFFEE8
FFC000
F8CF3A
FAE287
FDF2CF
FEFAEE
E54698
E96AAD
F1A4CE
F9D9EA
FCEFF6
A7469A
B969AE
D3A5CF
EDDBEB
F8F0F9
6B429C
8869AF
B7A5CE
E3DAEB
F3F0F8

```html
<!DOCTYPE html>
<html lang="en">
<head>
<meta charset="utf-8">
<title>LunoVix</title>
<link href="https://fonts.googleapis.com/css2?family=Press+Start+2P&display=swap" rel="stylesheet">
<style>
  :root {
    --space-black: #030306;
    --nebula-purple: #6B429C;
    --nebula-magenta: #A7469A;
    --star-blue: #0094D4;
    --logo-green: #82FF00;
    --signal-yellow: #FFF600;
    --button-white: #FFFFFF;
    --button-pink: #E54698;
    --button-ink: #3B1FA0;
  }
  * { margin: 0; padding: 0; box-sizing: border-box; }
  html, body {
    width: 1200px;
    height: 853px;
    overflow: hidden;
    background: var(--space-black);
    font-family: "Press Start 2P", monospace;
  }
  .hero {
    position: relative;
    width: 1200px;
    height: 853px;
    overflow: hidden;
  }
  .galaxy-backdrop {
    position: absolute;
    inset: 0;
    background:
      radial-gradient(ellipse 150px 110px at 600px 450px, rgba(167,70,154,0.55), transparent 70%),
      radial-gradient(ellipse 330px 240px at 620px 420px, rgba(107,66,156,0.45), transparent 75%),
      radial-gradient(ellipse 90px 120px at 260px 480px, rgba(0,148,212,0.25), transparent 70%),
      radial-gradient(circle 30px at 892px 496px, rgba(0,148,212,0.45), transparent 70%),
      radial-gradient(ellipse 520px 380px at 600px 430px, rgba(40,20,70,0.6), transparent 80%),
      var(--space-black);
  }
  .welcome {
    position: absolute;
    left: 53px;
    top: 30px;
    font-size: 15px;
    color: var(--signal-yellow);
    letter-spacing: 0.5px;
  }
  .cursor-blip {
    position: absolute;
    left: 330px;
    top: 292px;
    width: 12px;
    height: 4px;
    background: #dcdcdc;
  }
  .brand-name {
    position: absolute;
    left: 0;
    right: 0;
    top: 335px;
    text-align: center;
    font-size: 60px;
    color: var(--logo-green);
  }
  .shop-button {
    position: absolute;
    left: 474px;
    top: 462px;
    width: 250px;
    height: 62px;
    display: flex;
    align-items: center;
    justify-content: center;
    text-decoration: none;
    color: var(--button-ink);
    font-size: 15px;
  }
  .shop-button svg {
    position: absolute;
    inset: 0;
  }
  .shop-button span { position: relative; }
  .social-links {
    position: absolute;
    right: 50px;
    top: 792px;
    display: flex;
    gap: 18px;
    list-style: none;
  }
  .social-links a {
    display: flex;
    align-items: center;
    gap: 6px;
    color: var(--signal-yellow);
    text-decoration: none;
    font-size: 8px;
  }
  .social-links a::before {
    content: "";
    width: 10px;
    height: 10px;
    border: 2px solid var(--signal-yellow);
    border-radius: 50%;
  }
</style>
</head>
<body>
  <main class="hero">
    <div class="galaxy-backdrop" role="img" aria-label="Deep space photograph of a purple nebula surrounded by scattered blue and white stars"></div>

    <p class="welcome">Welcome to LunoVix</p>
    <div class="cursor-blip"></div>

    <h1 class="brand-name">LunoVix</h1>

    <a class="shop-button" href="#shop">
      <svg width="250" height="62" viewBox="0 0 250 62" aria-hidden="true">
        <polygon points="27,0 250,0 223,62 0,62" fill="var(--button-pink)"/>
        <polygon points="27,0 246,0 220,58 0,58" fill="var(--button-white)"/>
      </svg>
      <span>Visit Shop</span>
    </a>

    <ul class="social-links">
      <li><a href="#chatter">Chatter</a></li>
      <li><a href="#reelbox">Reelbox</a></li>
      <li><a href="#pixgram">Pixgram</a></li>
    </ul>
  </main>
</body>
</html>
```